Northfield Builders Guild Business card

We are looking for a new business card design with photo included.
Our business is a nonprofit construction contractor membership organization. We offer business education, assist with business setup and licensing, provide safety training, and provide a member directory.
URL: www.brickwayguildnetwork.org
Color code:
CMYK: 0 cyan, 42 magenta, 100 yellow, 0 black for Print.
Hexidecimal: #FF9900
RGB: R 255; G 153; B 0

```html
<!DOCTYPE html>
<html lang="en">
<head>
<meta charset="UTF-8">
<title>Northfield Builders Guild – Business Card</title>
<link href="https://fonts.googleapis.com/css2?family=Open+Sans:wght@400;600;800&family=Montserrat:wght@600&display=swap" rel="stylesheet">
<style>
  :root {
    --backdrop: #3a3a3a;
    --card-white: #ffffff;
    --brand-orange: #f89b1f;
    --ink-dark: #333132;
    --ink-text: #3b3b3b;
  }
  * { margin: 0; padding: 0; box-sizing: border-box; }
  html, body {
    width: 1200px; height: 780px; overflow: hidden;
    background: var(--backdrop);
    font-family: "Open Sans", Arial, sans-serif;
  }
  .card {
    position: absolute; left: 100px; top: 120px;
    width: 1000px; height: 540px;
    border-radius: 40px; overflow: hidden;
    background: var(--card-white);
  }
  .card-waves { position: absolute; inset: 0; width: 1000px; height: 540px; }
  .brand-name {
    position: absolute; left: 120px; top: 305px;
    width: 340px;
    font-family: "Open Sans", Arial, sans-serif;
    font-weight: 800; font-size: 37px; line-height: 1.05;
    color: var(--ink-dark); letter-spacing: -0.3px;
    white-space: nowrap;
  }
  .divider {
    position: absolute; left: 500px; top: 230px;
    width: 2px; height: 255px; background: var(--brand-orange);
  }
  .person { position: absolute; left: 515px; top: 180px; }
  .person-name {
    font-family: "Montserrat", Arial, sans-serif; font-weight: 600;
    font-size: 24px; letter-spacing: 7px; color: var(--brand-orange);
    line-height: 1;
  }
  .person-title { font-size: 14px; color: var(--ink-text); margin-top: 2px; }
  .address {
    position: absolute; left: 530px; top: 262px;
    font-size: 19px; line-height: 1.4; color: var(--ink-text);
  }
  .contacts { position: absolute; left: 545px; top: 355px; list-style: none; }
  .contact-item {
    display: flex; align-items: center; gap: 14px;
    height: 40px; font-size: 17px; color: var(--ink-text);
  }
  .contact-icon { width: 24px; height: 24px; flex: none; }
</style>
</head>
<body>
  <section class="card">
    <svg class="card-waves" viewBox="0 0 1000 540" aria-hidden="true">
      <rect width="1000" height="540" fill="var(--brand-orange)"/>
      <path d="M0,92 C300,12 720,18 1000,268 L1000,540 L0,540 Z" fill="var(--ink-dark)"/>
      <path d="M0,98 C300,30 700,36 1000,305 L1000,540 L0,540 Z" fill="var(--card-white)"/>
    </svg>

    <div class="brand-name">NORTHFIELD<br>BUILDERS GUILD</div>

    <div class="divider"></div>

    <div class="person">
      <p class="person-name">DANIEL REYES</p>
      <p class="person-title">CEO/Managing Director</p>
    </div>

    <p class="address">118 Larkspur Road Suite 210<br>Fairhaven OH 44012</p>

    <ul class="contacts">
      <li class="contact-item">
        <svg class="contact-icon" viewBox="0 0 24 24" aria-hidden="true">
          <path d="M6.5 3 L9.5 3 L10.5 8 L8 9.5 C9 12 11.5 14.8 14.5 16 L16 13.5 L21 14.5 L21 17.5 C21 19 19.8 20.5 18 20.3 C10 19.5 4.5 14 3.7 6 C3.5 4.2 5 3 6.5 3 Z" fill="none" stroke="var(--brand-orange)" stroke-width="2" stroke-linejoin="round"/>
          <path d="M14 3.5 A6.5 6.5 0 0 1 20.5 10 M14 7 A3 3 0 0 1 17 10" fill="none" stroke="var(--brand-orange)" stroke-width="1.8"/>
        </svg>
        <span>555-014-3927</span>
      </li>
      <li class="contact-item">
        <svg class="contact-icon" viewBox="0 0 24 24" aria-hidden="true">
          <rect x="2" y="5" width="20" height="14" fill="var(--brand-orange)"/>
          <path d="M2 5 L12 13 L22 5 M2 19 L9.5 11 M22 19 L14.5 11" fill="none" stroke="#fff" stroke-width="1.4"/>
        </svg>
        <span>dreyes@northfieldmail.com</span>
      </li>
      <li class="contact-item">
        <svg class="contact-icon" viewBox="0 0 24 24" aria-hidden="true">
          <g fill="none" stroke="var(--brand-orange)" stroke-width="1.6">
            <circle cx="12" cy="12" r="9.5"/>
            <ellipse cx="12" cy="12" rx="4.5" ry="9.5"/>
            <path d="M2.5 12 H21.5 M4 7 H20 M4 17 H20 M12 2.5 V21.5"/>
          </g>
        </svg>
        <span>www.brickwayguildnetwork.org</span>
      </li>
    </ul>
  </section>
</body>
</html>
```